New Church Home Page and Content Page Design

Our church, Harbor Light Baptist Church www.hlbtvkx.org, needs an update for our online presence. The homepage design should provide the following 4 pieces of information above the fold:
1. Church location - 47 Pinecrest Hollow Lane in Chappaqua, NY, USA.
2. Service times and types Sunday school, children's church, etc..
3. A space for some text describing us and our beliefs - a Bible believing independent Baptist church.
4. photos of our members to give visitors an impression of what kind of people attend our church - a friendly group of culturally diverse people who love Jesus.

In addition to the homepage we need a design for internal pages of general content. The content page design should provide a lot of room for content and prominent navigation area. We will use this design to host pages with content such as:
A full description of our beliefs
A photo gallery
An event calendar
Embedded audio and video of past sermons
A member directory
etc.
Updates

Thanks everyone for your submissions. I'll be meeting with our Pastor tomorrow. I am working as fast as I can to review all the designs and come up with a short list for him. A decision should be close behind.

Target Market(s)

Local people looking for a church.

Industry/Entity Type

Church

Requirements
Must have
• 1. Place to show church location - Linden Vale county, North Harbor State, USA.
2. Place to list service times and types.
3. A space for some text describing us and our beliefs.
4. A place to display photos of our members (see also the nice to have section)
Nice to have
• Would be great if the member photos (#4 in must have section) displayed the images in some innovative way. I rather not have an ordinary carousel of images.

```html
<!DOCTYPE html>
<html lang="en">
<head>
<meta charset="utf-8">
<title>Harbor Light Baptist Church</title>
<link href="https://fonts.googleapis.com/css2?family=Arimo:wght@400;700&display=swap" rel="stylesheet">
<style>
:root{
  --navy:#173a63;
  --navy-dark:#0f2c4f;
  --nav-band:#1d4470;
  --title-blue:#1f4d86;
  --text-grey:#5a5a5a;
  --line:#d4d4d4;
  --footer-bg:#efefef;
  --footer-bar:#e4e4e4;
  --footer-text:#555;
  --white:#fff;
}
*{margin:0;padding:0;box-sizing:border-box}
html,body{width:900px;height:1200px;overflow:hidden;background:var(--white);font-family:"Arimo",Arial,sans-serif}
.canvas{position:relative;width:900px;height:1200px}
.abs{position:absolute}

/* header */
.brand{left:134px;top:9px;display:flex;align-items:center;gap:8px}
.brand-mark{width:36px;height:36px;background:var(--navy)}
.brand-name{color:var(--navy);font-weight:700;font-size:12px;line-height:13.5px;width:60px}
.search{left:547px;top:19px;width:159px;height:21px;border:1px solid #c9c9c9;border-radius:2px;font-size:8px;color:#888;padding:6px 8px}
.search svg{position:absolute;right:6px;top:4px}
.login{left:714px;top:19px;width:57px;height:21px;background:#4a4f57;border-radius:2px;color:#fff;font-size:8px;text-align:center;line-height:21px}

/* nav */
.nav{left:0;top:61px;width:900px;height:33px;background:linear-gradient(var(--nav-band),var(--navy-dark))}
.nav-item{top:0;height:33px;line-height:33px;color:#fff;font-size:9.5px;transform:translateX(-50%);white-space:nowrap}
.nav-active{left:129px;top:0;width:86px;height:33px;background:#0d2543}

/* hero */
.hero{left:129px;top:110px;width:643px;height:243px;background:linear-gradient(180deg,#a9c7de 0%,#5e7a4f 35%,#7a6a55 60%,#3f5a2c 100%)}
.hero-band{left:129px;top:312px;width:643px;height:41px;background:rgba(0,0,0,.45)}
.hero-caption{left:148px;top:325px;color:#fff;font-size:14px;font-weight:700;letter-spacing:.2px}
.hero-arrow{top:326px;width:18px;height:18px;background:#5b5b5b}

/* welcome */
.welcome-title{left:129px;top:375px;width:643px;text-align:center;color:var(--title-blue);font-size:13px;font-weight:400}
.welcome-text{left:145px;top:403px;width:611px;text-align:center;color:var(--text-grey);font-size:8.2px;line-height:15.3px}
.divider{left:129px;top:466px;width:643px;height:1px;background:var(--line)}

/* columns */
.col-title{top:485px;color:var(--title-blue);font-size:11.5px;font-weight:400}
.photo{width:198px;height:104px;top:512px}
.photo-service{left:129px;background:linear-gradient(180deg,#6f8a5c,#8c6b5a 55%,#3e6a2d)}
.photo-beliefs{left:353px;background:linear-gradient(180deg,#95a8a0,#6c6454 55%,#c9b43a)}
.service-list{left:130px;top:627px;list-style:none;color:var(--navy);font-size:8.6px;line-height:17.5px}
.beliefs-text{left:353px;top:627px;width:196px;color:var(--text-grey);font-size:7.8px;line-height:15.3px}
.read-more{top:680px;color:var(--navy);font-size:7.2px}
.member-arrows{left:754px;top:488px;color:#bbb;font-size:9px;letter-spacing:6px}
.member{width:59px}
.member-photo{width:59px;height:54px;border:1px solid #d8d8d8;padding:2px;background:#fff}
.member-photo span{display:block;width:100%;height:100%;background:linear-gradient(160deg,#9fb58a,#c9a79a 55%,#5d6d4d)}
.member-name{margin-top:5px;color:var(--navy);font-size:7.4px;text-align:center;white-space:nowrap}

/* map */
.map{left:129px;top:729px;width:643px;height:198px;background:#e8e5dc}
.map-card{left:427px;top:750px;width:114px;height:44px;background:#fff;box-shadow:0 1px 3px rgba(0,0,0,.25);color:var(--navy);font-size:7.5px;line-height:13.5px;padding:7px 0 0 14px;white-space:nowrap}
.pin{left:446px;top:800px}

/* footer */
.footer{left:0;top:960px;width:900px;height:202px;background:var(--footer-bg)}
.footer-col{top:981px}
.footer-col h3{color:var(--title-blue);font-weight:400;font-size:8.8px;margin-bottom:7px}
.footer-col ul{list-style:none}
.footer-col li{color:var(--footer-text);font-size:7px;line-height:15px}
.social li{display:flex;align-items:center;gap:6px;line-height:22.5px;height:22.5px}
.social i{display:block;width:16px;height:16px;border-radius:50%;background:#777}
.footer-bar{left:0;top:1162px;width:900px;height:38px;background:var(--footer-bar)}
.copyright{left:0;top:1177px;width:900px;text-align:center;color:var(--footer-text);font-size:7px}
</style>
</head>
<body>
<div class="canvas">

  <header>
    <div class="abs brand">
      <div class="brand-mark"></div>
      <div class="brand-name">Harbor Light Baptist Church</div>
    </div>
    <div class="abs search">Search :
      <svg width="12" height="12" viewBox="0 0 12 12"><circle cx="5" cy="5" r="3.6" fill="none" stroke="#9a9a9a" stroke-width="1.3"/><line x1="7.6" y1="7.6" x2="11" y2="11" stroke="#9a9a9a" stroke-width="1.5"/></svg>
    </div>
    <div class="abs login">LOGIN</div>
  </header>

  <nav class="abs nav">
    <div class="abs nav-active"></div>
    <span class="abs nav-item" style="left:173px">Home</span>
    <span class="abs nav-item" style="left:262px">Contact Us</span>
    <span class="abs nav-item" style="left:358px">Calendar</span>
    <span class="abs nav-item" style="left:450px">Ministries</span>
    <span class="abs nav-item" style="left:552px">Service Times</span>
    <span class="abs nav-item" style="left:676px">Sermons and Media</span>
  </nav>

  <section>
    <div class="abs hero" role="img" aria-label="Photo of the stone church building among trees and hedges"></div>
    <div class="abs hero-band"></div>
    <div class="abs hero-caption">HARBOR LIGHT BAPTIST CHURCH</div>
    <div class="abs hero-arrow" style="left:724px">
      <svg width="18" height="18" viewBox="0 0 18 18"><polyline points="10.5,5 6.5,9 10.5,13" fill="none" stroke="#fff" stroke-width="1.3"/></svg>
    </div>
    <div class="abs hero-arrow" style="left:743px">
      <svg width="18" height="18" viewBox="0 0 18 18"><polyline points="7.5,5 11.5,9 7.5,13" fill="none" stroke="#fff" stroke-width="1.3"/></svg>
    </div>
  </section>

  <section>
    <h1 class="abs welcome-title">Welcome to Harbor Light Baptist church</h1>
    <p class="abs welcome-text">It is a long established fact that a reader will be distracted by the readable content of a page when looking at its layout. The point of using Lorem Ipsum is that it has a more-or-less normal distribution of letters, as opposed to using 'Content here, content here', making it look like readable English. Many desktop publishing packages and web page editors now use Lorem Ipsum as their default model text, and a search...</p>
    <div class="abs divider"></div>
  </section>

  <section>
    <h2 class="abs col-title" style="left:130px">Service times and types</h2>
    <div class="abs photo photo-service" role="img" aria-label="Photo of the congregation gathered outdoors by the church"></div>
    <ul class="abs service-list">
      <li>Coffee and fellowship - 9.45 AM</li>
      <li>Sunday School - 10.00 AM</li>
      <li>Sunday Morning Worship - 11.00 AM</li>
      <li>Wednesday Bible study &amp; Prayer Time - 7.00 PM</li>
    </ul>

    <h2 class="abs col-title" style="left:354px">Our beliefs</h2>
    <div class="abs photo photo-beliefs" role="img" aria-label="Photo of the church front with yellow flowering shrubs"></div>
    <p class="abs beliefs-text">The verbal inspiration and authority of the Scriptures.<br>The Bible reveals God, the fall of man, the way of salva-<br>tion, and God's planned purpose throughout the ages.</p>
    <span class="abs read-more" style="left:355px">[ Read More + ]</span>

    <h2 class="abs col-title" style="left:575px;top:484px">Our members</h2>
    <span class="abs member-arrows">&lsaquo;&rsaquo;</span>

    <div class="abs member" style="left:576px;top:512px"><div class="member-photo" role="img" aria-label="Photo of church members"><span></span></div><div class="member-name">Elena Moreau</div></div>
    <div class="abs member" style="left:644px;top:512px"><div class="member-photo" role="img" aria-label="Photo of church members"><span></span></div><div class="member-name">Elena Moreau</div></div>
    <div class="abs member" style="left:712px;top:512px"><div class="member-photo" role="img" aria-label="Photo of church members"><span></span></div><div class="member-name">Elena Moreau</div></div>
    <div class="abs member" style="left:576px;top:594px"><div class="member-photo" role="img" aria-label="Photo of church members"><span></span></div><div class="member-name">Elena Moreau</div></div>
    <div class="abs member" style="left:644px;top:594px"><div class="member-photo" role="img" aria-label="Photo of church members"><span></span></div><div class="member-name">Elena Moreau</div></div>
    <div class="abs member" style="left:712px;top:594px"><div class="member-photo" role="img" aria-label="Photo of church members"><span></span></div><div class="member-name">Elena Moreau</div></div>
    <span class="abs read-more" style="left:580px">[ Read More + ]</span>
  </section>

  <section>
    <div class="abs map" role="img" aria-label="Street map of the neighbourhood around the church"></div>
    <div class="abs map-card">Linden Vale county,<br>North Harbor State, USA</div>
    <svg class="abs pin" width="12" height="18" viewBox="0 0 12 18"><path d="M6 17 L2 8 A5 5 0 1 1 10 8 Z" fill="#d3d0cb"/><circle cx="6" cy="5" r="3.5" fill="#d6246e"/></svg>
  </section>

  <footer>
    <div class="abs footer"></div>
    <div class="abs footer-col" style="left:131px"><h3>Welcome</h3><ul><li>Home</li><li>Contact Us</li><li>Calendar</li><li>Ministries</li><li>Service Times</li><li>Sermons and Media</li></ul></div>
    <div class="abs footer-col" style="left:273px"><h3>Contact us</h3><ul><li>Our Pastor</li><li>What We Believe</li><li>First Visit</li><li>How to Become a Member</li><li>Newsletter Registration</li><li>Resources</li><li>Service Times &amp; Directions</li></ul></div>
    <div class="abs footer-col" style="left:421px"><h3>Calendar</h3><ul><li>Current Series</li><li>Photo Galleries</li></ul></div>
    <div class="abs footer-col" style="left:543px"><h3>Ministries</h3><ul><li>Adult</li><li>Children</li><li>Student</li><li>Evangelistic Outreach</li><li>The Plan of Salvation</li><li>Who is Jesus</li><li>Resources</li><li>Current Series</li><li>Newsletter Registration</li><li>Photo Galleries</li></ul></div>
    <div class="abs footer-col social" style="left:678px"><h3>Follow Us :</h3><ul><li><i></i>: Friendline</li><li><i></i>: Chirpwave</li><li><i></i>Worknet</li><li><i></i>Circlespace</li></ul></div>
    <div class="abs footer-bar"></div>
    <div class="abs copyright">Copyright &copy; 2014. Harbor Light Baptist church. All rights reserved.</div>
  </footer>

</div>
</body>
</html>
```